Borealis Metaljoin Society Wordpress Theme and newsletter template

We at the BMS are looking to start a Wordpress website and also send out a newsletter (web). We have just completed a Logo design project with PixelMarket and we were so pleased with the results that we would like to see what the designers can come up with for a Wordpress theme and a template for an online newsletter. The theme has to support Icelandic letters. It also has to have a subscription option by email. We would need to have the option to add advertisement banners. The theme has to be easy to work with.
Below we have added a two websites for a example of what we are looking for: .
http://www.qmx.org/
http://www.truvek.no/
The newsletter has to have a similar theme as the website and will be used with MS Publisher.

Attached is the new BMS logo.
Updates

Target Market(s)

Welding association members, welding and metalworking industry, suppliers in welding industry, International welding community, other national welding associations, welding education community

Industry/Entity Type

Welding

Number of Pages Required

3 page

Requirements
Must have
• The KLÞR logo
• Icelandic letters
• email formpage
• Advertisement space/banners/buttons
• Easy to manage
• Compatible with Wordpress
Nice to have
• Welding pictures
• Nice graphics
Should not have
• Should not be dark and heavy set.

```html
<!DOCTYPE html>
<html lang="en">
<head>
<meta charset="utf-8">
<title>KLÞR Welding</title>
<link href="https://fonts.googleapis.com/css2?family=Roboto:wght@400;500;700&family=Open+Sans:wght@400;600&display=swap" rel="stylesheet">
<style>
:root{
  --sky:#8acfec;
  --blue:#1b8fd0;
  --navy:#1f4f87;
  --red:#d6262f;
  --ink:#222;
  --muted:#555;
  --line:#e3e3e3;
  --foot:#f2f2f2;
}
*{margin:0;padding:0;box-sizing:border-box}
html,body{width:765px;height:1200px;overflow:hidden;background:#fff}
body{position:relative;font-family:"Open Sans",Arial,sans-serif;color:var(--ink)}
.abs{position:absolute}
.city-backdrop{left:0;top:84px;width:765px;height:339px;background:linear-gradient(180deg,#e9eaec,#d7d9dc 60%,#e6e7e9)}
.site-header{left:0;top:0;width:765px;height:84px;background:#fff;border-bottom:1px solid #e6e6e6}
.brand{left:63px;top:18px;display:flex;align-items:center;gap:6px}
.brand-mark{width:14px;height:14px;border-radius:50%;background:var(--red)}
.brand-name{font:700 26px "Roboto",sans-serif;color:var(--blue);letter-spacing:1px}
.brand-sub{left:82px;top:57px;font:600 5px "Open Sans",sans-serif;color:var(--navy)}
.lang{left:618px;top:29px;width:85px;height:24px;border:1px solid #e2e2e2;font:400 8px "Open Sans",sans-serif;color:#444;display:flex;align-items:center;padding-left:8px;gap:6px}
.lang .flag{width:14px;height:9px;background:#2b4a8a}
.main-nav{left:63px;top:100px;width:639px;height:40px;background:var(--sky);display:flex;align-items:center}
.main-nav a{font:400 9px "Open Sans",sans-serif;color:#fff;text-decoration:none;padding:0 19px;height:40px;line-height:40px;border-right:1px solid rgba(255,255,255,.25)}
.main-nav a:last-child{border:0}
.hero{left:63px;top:140px;width:639px;height:309px;background:linear-gradient(100deg,#a8122c 0%,#d8243e 38%,#8a2a5a 62%,#2e4d7a 80%,#1c2b45 100%);overflow:hidden}
.hero-title{left:63px;top:96px;font:700 38px/1 "Roboto",sans-serif;color:#fff}
.hero-sub{left:63px;top:134px;font:700 26px/1 "Roboto",sans-serif;color:#fff}
.hero-text{left:61px;top:170px;width:250px;font:400 8.5px/14px "Open Sans",sans-serif;color:#fff}
.hero-arrow{width:24px;height:24px;border-radius:50%;background:rgba(0,0,0,.3);top:143px}
.partners{left:66px;top:481px;display:flex;gap:14px}
.partners span{width:79px;height:43px;border:1px solid #e1e1e1;background:#fafafa;display:flex;align-items:center;justify-content:center}
.partners span i{width:46px;height:12px;background:#cfcfcf;border-radius:2px}
.welcome-title{left:0;top:546px;width:765px;text-align:center;font:400 20px "Roboto",sans-serif}
.welcome-title b{font-weight:400;color:var(--blue)}
.welcome-text{left:130px;top:580px;width:505px;text-align:center;font:400 7px/13.5px "Open Sans",sans-serif;color:var(--muted)}
.card{top:640px;width:196px}
.card .photo{height:116px}
.card h3{margin-top:16px;font:400 8.5px "Roboto",sans-serif;text-transform:uppercase;color:#333}
.card p{margin-top:9px;font:400 6.6px/13px "Open Sans",sans-serif;color:var(--muted)}
.card a{display:block;margin-top:6px;font:400 7.5px "Roboto",sans-serif;color:var(--navy)}
.section-title{font:400 16px "Roboto",sans-serif;color:var(--navy);padding-bottom:11px;border-bottom:1px solid var(--line)}
.section-title em{font-style:normal;color:var(--red)}
.members-photo{left:63px;top:934px;width:165px;height:143px;background:linear-gradient(135deg,#c9b07a,#d84040 50%,#5aa0d0)}
.members-text{left:244px;top:932px;width:250px;font:400 6.6px/13px "Open Sans",sans-serif;color:#333}
.members-text p+p{margin-top:7px}
.more{left:244px;top:1070px;font:400 8px "Roboto",sans-serif;color:var(--navy);display:flex;align-items:center;gap:7px}
.news-item{left:524px;width:178px}
.news-item h4{font:400 9px "Roboto",sans-serif;color:var(--navy)}
.news-item .time{margin-top:9px;font:400 7px "Open Sans",sans-serif;color:#333;display:flex;align-items:center;gap:4px}
.news-item p{margin-top:8px;font:400 7px/13px "Open Sans",sans-serif;color:#444}
.news-sep{left:524px;top:1006px;width:178px;border-top:1px dashed #ddd}
.site-footer{left:0;top:1120px;width:765px;height:80px;background:var(--foot)}
.foot-brand{left:63px;top:1142px;display:flex;align-items:center;gap:4px;font:700 15px "Roboto",sans-serif;color:var(--blue)}
.foot-brand i{width:9px;height:9px;border-radius:50%;background:var(--red)}
.foot-head{font:400 12px "Roboto",sans-serif;color:#333}
.foot-small{font:400 7.5px/12.5px "Open Sans",sans-serif;color:#444}
.social{left:649px;top:1153px;display:flex;gap:3px}
.social i{width:15px;height:15px;background:#555;border-radius:3px}
</style>
</head>
<body>
<div class="abs city-backdrop" role="img" aria-label="Faded city skyline backdrop"></div>

<header class="abs site-header">
  <div class="abs brand"><span class="brand-mark"></span><span class="brand-name">KLÞR</span></div>
  <div class="abs brand-sub">KLÞR FÉLAGIÐ</div>
  <div class="abs lang"><span class="flag"></span>ENGLISH
    <svg width="7" height="5" viewBox="0 0 7 5" style="margin-left:8px"><path d="M1 1l2.5 2.5L6 1" stroke="#555" fill="none"/></svg></div>
</header>

<nav class="abs main-nav">
  <a>Home</a><a>About us</a><a>Members</a><a>Metalworking Industry</a><a>Welding</a><a>Services</a><a>Contact us</a>
</nav>

<section class="abs hero" role="img" aria-label="Welder in mask with sparks flying">
  <div class="abs hero-title">WELDING</div>
  <div class="abs hero-sub">Association</div>
  <p class="abs hero-text">Lorem ipsum dolor sit amet, consectetur adipiscing elit, sed do eiusmod tempor incididunt ut labore et dolore magna aliqua. Ut enim ad minim veniam, quis nostrud</p>
  <span class="abs hero-arrow" style="left:18px"><svg width="24" height="24"><path d="M14 7l-5 5 5 5" stroke="#fff" stroke-width="1.5" fill="none"/></svg></span>
  <span class="abs hero-arrow" style="left:597px"><svg width="24" height="24"><path d="M10 7l5 5-5 5" stroke="#fff" stroke-width="1.5" fill="none"/></svg></span>
</section>

<div class="abs partners"><span><i></i></span><span><i></i></span><span><i></i></span><span><i></i></span><span><i></i></span><span><i></i></span><span><i></i></span></div>

<h1 class="abs welcome-title">Welcome To <b>KLÞR Welding</b></h1>
<p class="abs welcome-text">Vestibulum commodo volutpat a, convallis ac, laoreet enim. Phasellus fermentum in, dolor pellentesque. Mulla imperdiet sit amet magna. Vestibulum dapibus, Vestibulum commodo volutpat a, convallis ac, laoreet enim. Phasellus fermentum in, dolor pellentesque. Mulla imperdiet sit amet magna. Vestibulum dapibus, Vestibulum commodo volutpat a, convallis ac, laoreet enim. Phasellus fermentum in.</p>

<article class="abs card" style="left:63px">
  <div class="photo" role="img" aria-label="Worker grinding metal with sparks" style="background:linear-gradient(135deg,#c8c4be,#b8382e 45%,#e8a25a 75%,#6a6058)"></div>
  <h3>Welding and metalworking industry</h3>
  <p>Lorem ipsum dolor sit amet, consectetur adipiscing elit, sed do eiusmod tempor incididunt ut labore et dolore magna Lorem ipsum dolor sit amet.</p>
  <a>READ MORE</a>
</article>
<article class="abs card" style="left:284px">
  <div class="photo" role="img" aria-label="Angle grinder throwing golden sparks" style="background:linear-gradient(135deg,#2a2420,#c98a2a 45%,#f0c060 60%,#3a3028)"></div>
  <h3>Suppliers in welding industry</h3>
  <p>Lorem ipsum dolor sit amet, consectetur adipiscing elit, sed do eiusmod tempor incididunt ut labore et dolore magna Lorem ipsum dolor sit amet.</p>
  <a>READ MORE</a>
</article>
<article class="abs card" style="left:505px">
  <div class="photo" role="img" aria-label="Two welders in helmets talking at a plant" style="background:linear-gradient(90deg,#8a929a,#3a4a70 35%,#b8bec4 60%,#2e3c66)"></div>
  <h3>International welding community</h3>
  <p>Lorem ipsum dolor sit amet, consectetur adipiscing elit, sed do eiusmod tempor incididunt ut labore et dolore magna Lorem ipsum dolor sit amet.</p>
  <a>READ MORE</a>
</article>

<h2 class="abs section-title" style="left:63px;top:888px;width:430px">Welding Association Members</h2>
<div class="abs members-photo" role="img" aria-label="Engineer in hard hat working on a turbine"></div>
<div class="abs members-text">
  <p>Lorem ipsum dolor sit amet, consectetur adipiscing elit, sed do eiusmod tempor incididunt ut labore et dolore magna aliqua. Ut enim ad minim veniam, quis nostrud exercitation Lorem ipsum dolor sit amet, consectetur adipiscing elit, sed do eiusmod tempor incididunt ut labore et dolore magna aliqua. Ut enim ad minim veniam,</p>
  <p>Lorem ipsum dolor sit amet, consectetur adipiscing elit, sed do eiusmod tempor incididunt ut labore et dolore magna aliqua. Ut enim ad minim veniam, quis nostrud exercitation Lorem ipsum dolor sit amet, consectetur adipiscing elit, sed do eiusmod tempor incididunt</p>
</div>
<div class="abs more">READ MORE <svg width="8" height="8"><circle cx="4" cy="4" r="4" fill="#1f4f87"/><path d="M3 2l2 2-2 2" stroke="#fff" fill="none"/></svg></div>

<h2 class="abs section-title" style="left:524px;top:888px;width:178px">Latest <em>News</em></h2>
<div class="abs news-item" style="top:929px">
  <h4>Nemo Enim Ipsam Voluptatem</h4>
  <div class="time"><svg width="7" height="7"><circle cx="3.5" cy="3.5" r="3" stroke="#222" fill="none"/><path d="M3.5 1.8v1.9h1.4" stroke="#222" fill="none" stroke-width=".8"/></svg>19.00 pm - 21.00 pm</div>
  <p>Vivamus elementum semper nisi. Lorem ipsum dolor sit amet, sectetuer adipiscing elit.</p>
</div>
<div class="abs news-sep"></div>
<div class="abs news-item" style="top:1017px">
  <h4>Nemo Enim Ipsam Voluptatem</h4>
  <div class="time"><svg width="7" height="7"><circle cx="3.5" cy="3.5" r="3" stroke="#222" fill="none"/><path d="M3.5 1.8v1.9h1.4" stroke="#222" fill="none" stroke-width=".8"/></svg>19.00 pm - 21.00 pm</div>
  <p>Vivamus elementum semper nisi. Lorem ipsum dolor sit amet, sectetuer adipiscing elit.</p>
</div>

<footer class="abs site-footer"></footer>
<div class="abs foot-brand"><i></i>KLÞR</div>
<div class="abs" style="left:137px;top:1141px">
  <div class="foot-head">COPYRIGHT</div>
  <div class="foot-small">(c) 2015 klþr welding. All rights reserved.</div>
</div>
<div class="abs" style="left:328px;top:1135px">
  <div class="foot-head">ADDRESS</div>
  <div class="foot-small">welding association PO Box 4410,<br>Northvale 3091</div>
</div>
<div class="abs foot-small" style="left:487px;top:1148px;line-height:16px">
  <div style="display:flex;gap:10px;align-items:center"><svg width="10" height="10"><path d="M2 1l2 0 1 2.5-1.2 1a6 6 0 0 0 2.7 2.7l1-1.2L10 8v1.5c-4 .5-8.5-4-8-8.5z" stroke="#d6262f" fill="none" stroke-width=".9"/></svg>+1 0555 202 318</div>
  <div style="display:flex;gap:10px;align-items:center"><svg width="10" height="8"><rect x=".5" y=".5" width="9" height="7" stroke="#d6262f" fill="none"/><path d="M.5 .5l4.5 4 4.5-4" stroke="#d6262f" fill="none"/></svg>info@metaljoinsociety.org</div>
</div>
<div class="abs social"><i></i><i></i><i></i></div>
</body>
</html>
```